Business Card Design Project for Lumen Glow & Medispa

This is a project for a Medispa, where offers service such as massage, facial, IPL treatment, skin rejuvenation. The interior design colour is purple, but I wish not only purple, we can also add some other colour into the design to make it more interesting.

Would be great if the business could be elegant and relaxing feel, instead of the serious business cards. The card is more like a display ticket for customers to park and prevent their card be towed away.

I have uploaded some inspiration samples and logo for your design.

This card will be a general card without any specific person's name on it.
Contents include:
Add: 19C Harrowfield Lane, Auckland 1043
P: 09 472 5163
WeChat ID: lumenglowspa
Web: www.lumenglow-example.co,nz

Target Market(s)

80% female and 20% male market. Female at all age, mostly asian, but we are trying to expand the market to Kiwis also.

Industry/Entity Type

Business

Font styles to use
Sans Serif
Script

Requirements
Must have
• Floral background or decoration. Prefer watercolour design, but if have any other better idea will do.
To make it unique from other business cards, as it is more for parking display.
Nice to have
• keep is simple as well, please don't put too many different decorations.
Should not have
• Black or dark colour as background.

```html
<!DOCTYPE html>
<html lang="en">
<head>
<meta charset="utf-8">
<title>Lumen Glow &amp; Medispa – Business Card</title>
<link rel="stylesheet" href="https://fonts.googleapis.com/css2?family=Raleway:wght@300&family=Cormorant+Garamond:wght@400;500&display=swap">
<style>
  :root {
    --stage: #ecebee;
    --card-white: #ffffff;
    --plum-deep: #5e1a6c;
    --plum: #7f2787;
    --orchid: #a8479f;
    --lilac: #c98bc6;
    --lilac-pale: #f1e2ef;
    --grey-text: #8d8a90;
    --white-soft: rgba(255,255,255,0.94);
    --white-faint: rgba(255,255,255,0.5);
    --white-label: rgba(255,255,255,0.38);
  }
  * { box-sizing: border-box; margin: 0; padding: 0; }
  html, body {
    width: 1200px; height: 800px; overflow: hidden;
    background: var(--stage);
  }
  .canvas {
    position: relative; width: 1200px; height: 800px;
    display: flex; justify-content: center; align-items: center; gap: 80px;
  }
  .card {
    position: relative; width: 320px; height: 640px; overflow: hidden;
    box-shadow: 0 6px 24px rgba(60,20,70,0.18);
  }

  /* Shared brand block */
  .brand {
    position: absolute; left: 0; right: 0; text-align: center;
    font-family: "Raleway", sans-serif; font-weight: 300;
    font-size: 24px; line-height: 1.3; letter-spacing: 0.04em;
  }
  .brand__dot {
    display: block; width: 54px; height: 54px; margin: 0 auto 16px;
    border-radius: 50%;
  }

  /* Floral illustration area (placeholder wash in its main tones) */
  .floral { position: absolute; }

  /* Front */
  .card--front {
    background: linear-gradient(to bottom, var(--card-white) 0%, var(--card-white) 44%, var(--lilac-pale) 58%, var(--lilac) 80%, var(--orchid) 100%);
  }
  .card--front .brand { top: 130px; color: var(--grey-text); }
  .card--front .brand__dot { background: var(--orchid); }
  .card--front .floral {
    left: 30px; right: 20px; top: 300px; bottom: 20px;
    border-radius: 46% 54% 40% 60% / 38% 42% 58% 62%;
    background:
      radial-gradient(ellipse 40% 22% at 35% 30%, rgba(255,255,255,0.95) 0%, rgba(255,255,255,0.5) 55%, transparent 100%),
      radial-gradient(ellipse 18% 10% at 38% 8%, rgba(255,255,255,0.85) 0%, transparent 100%),
      radial-gradient(ellipse 45% 20% at 65% 85%, rgba(255,255,255,0.8) 0%, transparent 100%),
      linear-gradient(to bottom, rgba(236,214,234,0.6), rgba(201,139,198,0.5));
  }

  /* Back */
  .card--back {
    background: linear-gradient(160deg, var(--plum) 0%, var(--orchid) 45%, var(--plum) 75%, var(--plum-deep) 100%);
  }
  .card--back .brand { top: 50px; color: var(--white-faint); }
  .card--back .brand__dot { background: rgba(255,255,255,0.3); }
  .card--back .floral {
    left: 60px; right: 30px; top: 200px; height: 230px;
    border-radius: 50% 50% 44% 56% / 40% 40% 60% 60%;
    background:
      radial-gradient(ellipse 32% 16% at 35% 18%, rgba(255,255,255,0.32) 0%, transparent 100%),
      radial-gradient(ellipse 40% 20% at 38% 48%, rgba(255,255,255,0.3) 0%, transparent 100%),
      radial-gradient(ellipse 25% 40% at 85% 70%, rgba(255,255,255,0.16) 0%, transparent 100%),
      rgba(255,255,255,0.05);
  }
  .contact {
    position: absolute; left: 20px; right: 22px; top: 468px;
    list-style: none;
    font-family: "Cormorant Garamond", serif;
  }
  .contact__row {
    display: flex; justify-content: space-between; align-items: baseline;
    gap: 10px; line-height: 1.25;
  }
  .contact__label {
    flex: none; font-size: 10px; color: var(--white-label); letter-spacing: 0.05em;
  }
  .contact__value {
    font-size: 16px; font-weight: 500; color: var(--white-soft); text-align: right;
    white-space: nowrap;
  }
  .contact__row--phone .contact__value { font-size: 19px; }
  .contact__row--address .contact__value { font-size: 15px; }
</style>
</head>
<body>
<main class="canvas">
  <section class="card card--front" aria-label="Card front">
    <div class="brand"><span class="brand__dot"></span>Lumen Glow &amp; Medispa</div>
    <div class="floral" role="img" aria-label="Floral illustration: white line-art daisies on a slender stem with long sweeping leaves over a soft lilac watercolour wash"></div>
  </section>

  <section class="card card--back" aria-label="Card back">
    <div class="brand"><span class="brand__dot"></span>Lumen Glow &amp; Medispa</div>
    <div class="floral" role="img" aria-label="Floral illustration: two faint pale daisies on a curved stem with translucent leaves over the purple background"></div>
    <ul class="contact">
      <li class="contact__row contact__row--phone"><span class="contact__label">phone</span><span class="contact__value">09 472 5163</span></li>
      <li class="contact__row"><span class="contact__label">web</span><span class="contact__value">www.lumenglow-example.co,nz</span></li>
      <li class="contact__row"><span class="contact__label">wechat ID</span><span class="contact__value">lumenglowspa</span></li>
      <li class="contact__row contact__row--address"><span class="contact__label">address</span><span class="contact__value">19C Harrowfield Lane, Auckland 1043</span></li>
    </ul>
  </section>
</main>
</body>
</html>
```